Business Card Design Project

Small privately owned salon.

Industry/Entity Type

Business

Contact Information for Business Card

Hair salon.i would like my logo to be my name , Marisol Denby. Address and phone can go on the front or back. The back will be where I write their appt.
address-362 Thistledown lane York, Pa. 17488
Phone- 717-555-0148

```html
<!DOCTYPE html>
<html lang="en">
<head>
<meta charset="utf-8">
<title>Marisol Denby – Business Card</title>
<link rel="stylesheet" href="https://fonts.googleapis.com/css2?family=Didact+Gothic&display=swap">
<style>
  :root {
    --backdrop: #2b2929;
    --card: #ffffff;
    --ink: #1a1a1a;
    --ink-soft: #555555;
    --rule: #9a9a9a;
    --font-body: "Didact Gothic", "Century Gothic", sans-serif;
  }
  * { box-sizing: border-box; margin: 0; padding: 0; }
  html, body {
    width: 1200px;
    height: 1200px;
    overflow: hidden;
    background: var(--backdrop);
    font-family: var(--font-body);
    color: var(--ink);
  }
  .sheet {
    position: relative;
    width: 1200px;
    height: 1200px;
  }
  .card {
    position: absolute;
    left: 230px;
    width: 740px;
    height: 423px;
    background: var(--card);
  }
  .card--back { top: 110px; }
  .card--front { top: 667px; }

  /* Back: appointment card */
  .appt-label {
    position: absolute;
    left: 46px;
    top: 40px;
    font-size: 19px;
    color: var(--ink-soft);
  }
  .appt-lines {
    position: absolute;
    left: 62px;
    right: 46px;
    top: 92px;
  }
  .appt-line {
    height: 1px;
    background: var(--rule);
    margin-bottom: 54px;
  }
  .card--back .brand-name {
    position: absolute;
    right: 60px;
    bottom: 44px;
    font-size: 40px;
  }

  /* Front */
  .card--front .brand-name {
    position: absolute;
    left: 0;
    right: 0;
    top: 150px;
    text-align: center;
    font-size: 54px;
  }
  .brand-name {
    font-family: var(--font-body);
    font-weight: 400;
    color: var(--ink);
    letter-spacing: 1px;
  }
  .contact-phone {
    position: absolute;
    left: 40px;
    top: 300px;
    font-size: 19px;
    color: var(--ink-soft);
  }
  .contact-address {
    position: absolute;
    right: 40px;
    bottom: 38px;
    font-size: 19px;
    color: var(--ink-soft);
  }
</style>
</head>
<body>
  <main class="sheet">
    <section class="card card--back" aria-label="Appointment card, back side">
      <p class="appt-label">Appointment:</p>
      <div class="appt-lines">
        <div class="appt-line"></div>
        <div class="appt-line"></div>
        <div class="appt-line"></div>
        <div class="appt-line"></div>
      </div>
      <p class="brand-name">Marisol Denby</p>
    </section>

    <section class="card card--front" aria-label="Business card, front side">
      <h1 class="brand-name">Marisol Denby</h1>
      <p class="contact-phone">717-555-0148</p>
      <p class="contact-address">362 Thistledown lane York, Pa. 17488</p>
    </section>
  </main>
</body>
</html>
```